Online trading school - Website design

We are building an online trading school (trading of shares, commodities, indices, currencies). The purpose is to teach online traders how to trade successfully. We need to design the homepage of the website and logo (bramwelloq.com will be the domain). The homepage will contain the following elements

- logo
- Sign in and Register links/buttons
- upper menu
- short introduction
- a couple of bullet points 'Why to join our school?'
- sign up form
- text
- bottom menu

Attached is a draft for the designer. The draft is just for an inspiration, the actual structure of the website can be different if the designer thinks so.

The designer is free to choose colors.

School

3 page

```html
<!DOCTYPE html>
<html lang="en">
<head>
<meta charset="utf-8">
<title>Bramwelloq – Online Trading School</title>
<link rel="stylesheet" href="https://fonts.googleapis.com/css2?family=Montserrat:wght@400;600;700&family=Open+Sans:wght@400;600&display=swap">
<style>
  :root {
    --navy-deep: #0a2c52;
    --navy: #0d3f75;
    --blue: #16609f;
    --blue-panel: #1a6aa9;
    --ink-dark: #222222;
    --text-grey: #666666;
    --page-bg: #eef0f2;
    --white: #ffffff;
    --field: #f4f5f6;
  }
  * { box-sizing: border-box; margin: 0; padding: 0; }
  html, body { width: 1200px; height: 630px; overflow: hidden; }
  body {
    background: var(--page-bg);
    font-family: "Open Sans", Arial, sans-serif;
    color: var(--ink-dark);
    position: relative;
  }

  /* Top contact bar */
  .topbar {
    position: absolute; left: 0; top: 0; width: 1200px; height: 28px;
    background: var(--navy-deep);
    color: #d8e3ef; font-size: 9px;
    display: flex; align-items: center; justify-content: space-between;
    padding: 0 222px;
  }
  .contact-list { display: flex; gap: 20px; align-items: center; }
  .contact-item { display: flex; align-items: center; gap: 5px; }
  .contact-item svg { width: 9px; height: 10px; fill: #d8e3ef; }
  .social { display: flex; align-items: center; gap: 7px; }
  .social-dot { width: 9px; height: 9px; border-radius: 50%; background: #d8e3ef; }

  /* Header */
  .header {
    position: absolute; left: 0; top: 28px; width: 1200px; height: 137px;
    background: linear-gradient(180deg, var(--navy) 0%, var(--blue) 100%);
  }
  .account-links {
    position: absolute; right: 226px; top: 11px; display: flex; gap: 8px;
  }
  .account-btn {
    border: 1px solid #c9d9ea; color: var(--white);
    font-size: 8.5px; line-height: 1.2; padding: 3px 12px; border-radius: 2px;
  }
  .brand {
    position: absolute; left: 238px; top: 26px;
    display: flex; align-items: center; gap: 10px;
  }
  .brand-mark { width: 22px; height: 22px; background: var(--white); }
  .brand-name {
    font-family: "Montserrat", Arial, sans-serif; font-weight: 700;
    font-size: 22px; line-height: 26px; color: var(--white); letter-spacing: 0.3px;
  }
  .main-nav {
    position: absolute; right: 232px; top: 43px; display: flex; gap: 16px;
    font-size: 9.5px; line-height: 13px; color: var(--white); font-weight: 600;
  }

  /* Scenic band behind hero */
  .stage {
    position: absolute; left: 0; top: 165px; width: 1200px; height: 210px;
    background: linear-gradient(180deg, #dfe4ea 0%, #f3f5f7 60%, #e9ecef 100%);
  }

  /* Hero block */
  .hero {
    position: absolute; left: 222px; top: 100px; width: 756px; height: 268px;
    background: var(--white); padding: 6px; display: flex; gap: 4px;
  }
  .hero-visual {
    width: 512px; height: 256px;
    background: radial-gradient(ellipse at 60% 40%, #1d6aa0 0%, #0c3b66 55%, #071f3a 100%);
  }
  .signup { flex: 1; background: var(--blue-panel); padding: 20px 14px; }
  .signup-title {
    font-family: "Montserrat", Arial, sans-serif; font-weight: 700;
    font-size: 17px; color: var(--white); margin-bottom: 14px;
  }
  .field {
    background: var(--field); height: 30px; width: 194px; margin-bottom: 8px;
    font-size: 9.5px; color: #333; padding: 9px 10px;
  }
  .agree {
    display: flex; align-items: center; gap: 8px; color: var(--white);
    font-size: 9px; margin: 6px 0 12px;
  }
  .agree-box { width: 12px; height: 12px; background: var(--white); }
  .submit {
    display: inline-block; background: var(--ink-dark); color: var(--white);
    font-family: "Montserrat", Arial, sans-serif; font-weight: 600;
    font-size: 10px; padding: 9px 20px;
  }

  /* Features */
  .features {
    position: absolute; left: 222px; top: 385px; width: 756px;
    display: flex; justify-content: space-between; padding: 0 8px;
  }
  .feature { width: 140px; text-align: center; }
  .feature-icon {
    width: 28px; height: 28px; border-radius: 50%; background: var(--navy);
    margin: 0 auto 8px; display: flex; align-items: center; justify-content: center;
  }
  .feature-icon svg { width: 14px; height: 14px; fill: none; stroke: var(--white); stroke-width: 1.6; }
  .feature-title {
    font-family: "Montserrat", Arial, sans-serif; font-weight: 700;
    font-size: 9.5px; color: var(--navy); line-height: 1.3; margin-bottom: 6px;
  }
  .feature-text { font-size: 8px; color: var(--text-grey); line-height: 1.4; }

  /* Offer band */
  .offer {
    position: absolute; left: 0; top: 495px; width: 1200px; height: 135px;
    background: linear-gradient(180deg, #0c3a6c 0%, var(--navy-deep) 100%);
    text-align: center; color: var(--white); padding-top: 30px;
  }
  .offer-title {
    font-family: "Montserrat", Arial, sans-serif; font-weight: 400;
    font-size: 22px; letter-spacing: 0.5px; margin-bottom: 16px;
  }
  .offer-text {
    width: 620px; margin: 0 auto; font-size: 11px; line-height: 1.45; color: #e2ebf4;
  }
</style>
</head>
<body>

<div class="topbar">
  <div class="contact-list">
    <span class="contact-item">
      <svg viewBox="0 0 10 12"><path d="M5 0a4 4 0 0 0-4 4c0 3 4 8 4 8s4-5 4-8a4 4 0 0 0-4-4zm0 5.5A1.5 1.5 0 1 1 5 2.5a1.5 1.5 0 0 1 0 3z"/></svg>
      Lindenweg 14 50321 Arnsfeld
    </span>
    <span class="contact-item">
      <svg viewBox="0 0 8 12"><rect x="0" y="0" width="8" height="12" rx="1.5"/><rect x="1.5" y="1.5" width="5" height="7.5" fill="#0a2c52"/></svg>
      +49 (0)4417 512
    </span>
    <span class="contact-item">
      <svg viewBox="0 0 12 9"><rect width="12" height="9" rx="1"/><path d="M0.5 1l5.5 4 5.5-4" stroke="#0a2c52" stroke-width="1.2" fill="none"/></svg>
      info@bramwelloq.com
    </span>
  </div>
  <div class="social">
    <span>Connect with Us</span>
    <span class="social-dot"></span>
    <span class="social-dot"></span>
    <span class="social-dot"></span>
    <span class="social-dot"></span>
  </div>
</div>

<header class="header">
  <div class="account-links">
    <span class="account-btn">Sign in</span>
    <span class="account-btn">Register</span>
  </div>
  <div class="brand">
    <span class="brand-mark"></span>
    <span class="brand-name">BRAMWELLOQ</span>
  </div>
  <nav class="main-nav">
    <span>Home</span>
    <span>About our school</span>
    <span>Risk warning</span>
    <span>FAQ</span>
    <span>Trading Glossary</span>
    <span>Contact</span>
  </nav>
</header>

<div class="stage"></div>

<section class="hero">
  <div class="hero-visual" role="img" aria-label="Trader in a suit presenting rising market charts over a glowing world map"></div>
  <form class="signup">
    <h2 class="signup-title">JOIN SCHOOL NOW!</h2>
    <div class="field">First name</div>
    <div class="field">Last name</div>
    <div class="field">Email</div>
    <div class="agree"><span class="agree-box"></span>Agree with our terms and conditions</div>
    <span class="submit">Submit</span>
  </form>
</section>

<section class="features">
  <div class="feature">
    <div class="feature-icon"><svg viewBox="0 0 14 14"><circle cx="7" cy="6" r="3.5"/><path d="M5.5 11h3M6 13h2"/></svg></div>
    <h3 class="feature-title">BEST TRADING<br>TIPS EVER</h3>
    <p class="feature-text">Consectetur adipisicing elit, sed do eiusmod teor incididunt.</p>
  </div>
  <div class="feature">
    <div class="feature-icon"><svg viewBox="0 0 14 14"><path d="M2 12l5-5M7 7l3-5 2 2-5 3"/></svg></div>
    <h3 class="feature-title">SECRET TIPS<br>FROM EXPERT</h3>
    <p class="feature-text">Lorem ipsum dolor sit amet, consectetur adipisicing elit.</p>
  </div>
  <div class="feature">
    <div class="feature-icon"><svg viewBox="0 0 14 14"><rect x="1.5" y="2.5" width="11" height="7.5"/><path d="M5 12.5h4M3.5 8l2.5-2.5 2 1.5 2.5-3"/></svg></div>
    <h3 class="feature-title">WE TEACH YOU HOW<br>TO TRADE ONLINE</h3>
    <p class="feature-text">Do eiusmod tempor incididunt ut labore et dolore mna aliqua.</p>
  </div>
  <div class="feature">
    <div class="feature-icon"><svg viewBox="0 0 14 14"><circle cx="7" cy="7" r="5"/><path d="M7 4v3l2 2"/></svg></div>
    <h3 class="feature-title">LEARN HOW TO<br>TRADE COMMODITIES</h3>
    <p class="feature-text">Sed do eiusmod tempor incididunt ut labore et dolore.</p>
  </div>
  <div class="feature">
    <div class="feature-icon"><svg viewBox="0 0 14 14"><circle cx="7" cy="5" r="2.5"/><path d="M2.5 12.5c0-3 2-4.5 4.5-4.5s4.5 1.5 4.5 4.5"/></svg></div>
    <h3 class="feature-title">LEARN HOW TO<br>BECOME A TRADER</h3>
    <p class="feature-text">Consectetur adipisicing elit, sed do eiusmod tempor incididunt.</p>
  </div>
</section>

<section class="offer">
  <h2 class="offer-title">WHAT DO WE OFFER</h2>
  <p class="offer-text">Nemo enim ipsam voluptatem quia voluptas sit aspernatur aut odit aut fugit, sed quia consequuntur magni dolores eos qui ratione voluptatem sequi nesciunt. Neque porro quisquam est, qui dolorem ipsum quia dolor sit amet, consectetur, adipisci velit, sed quia non numquam eius modi tempora incidunt.</p>
</section>

</body>
</html>
```